PL regenerative food process graphic design for posters

We are a Hawaii snorkel tour company who makes all of our cruises vegan food from scratch and have a family farm we use for composting & growing food products. We want a design showing our food recycling process. From the soil to the tree's fruit to cooking, to eating, to zero-waste trash can, to recycle, to compost pile. Representing the complete circle in the process. We want you to use a breadfruit or ulu tree for our tree. We want to express our companies commitment to being good stewards to Hawaii and our planet's environmental health.

Target Market(s)

tourists, families traveling

Industry/Entity Type

Eco-tourism

Font styles to use
Sans Serif

Colors
59FF00
82FF00
B8FF75
E3FFCB
F4FFEA
FFC000
F8CF3A
FAE287
FDF2CF
FEFAEE

Requirements
Must have
• Small Pine Lark logo on artwork showing ownership, Hand drawn artwork, with written explanation at each step of the process
Nice to have
• easy to understand artwork showing the process from farm to table and back again
Should not have
• stock images, graphics, photos

```html
<!DOCTYPE html>
<html lang="en">
<head>
<meta charset="utf-8">
<title>Pine Lark – ʻāina, That which feed us</title>
<link href="https://fonts.googleapis.com/css2?family=Barlow+Condensed:wght@400;600;700&family=Barlow+Semi+Condensed:wght@400;700&family=Dancing+Script:wght@600&display=swap" rel="stylesheet">
<style>
  :root{
    --page:#c8c8c8;
    --paper:#ffffff;
    --navy:#1f3f84;
    --red:#e2334b;
    --teal:#1aa7b3;
    --sky:#e2f3fb;
    --ink:#222222;
    --label:#1b1b1b;
    --tree-a:#b8c4cc;
    --tree-b:#8a99a3;
  }
  *{margin:0;padding:0;box-sizing:border-box}
  html,body{width:1200px;height:1200px;overflow:hidden;background:var(--page)}
  .poster{position:absolute;left:52px;top:198px;width:1096px;height:772px;background:var(--paper);overflow:hidden;
    font-family:"Barlow Semi Condensed","Barlow Condensed",sans-serif;color:var(--ink)}
  .header-shapes{position:absolute;left:0;top:0}
  .brand{position:absolute;left:34px;top:22px;color:#fff;font-family:"Barlow Condensed",sans-serif;font-weight:600;font-size:58px;letter-spacing:1px;line-height:1}
  .headline-word{position:absolute;left:580px;top:6px;height:70px;display:flex;align-items:center;color:#fff;font-family:"Dancing Script",cursive;font-size:54px;font-weight:600;line-height:1}
  .headline-tag{position:absolute;left:826px;top:6px;height:70px;display:flex;align-items:center;color:#fff;font-family:"Barlow Condensed",sans-serif;font-weight:700;font-size:31px;letter-spacing:.2px;white-space:nowrap}
  .bottom-rule{position:absolute;left:0;right:0;bottom:0;height:7px;background:var(--teal)}
  .cycle{position:absolute;left:0;top:0}
  .step-label{position:absolute;width:130px;text-align:center;font-family:"Barlow Condensed",sans-serif;font-weight:700;font-size:17px;line-height:1.05;color:var(--label)}
  .note{position:absolute;font-size:13.4px;line-height:1.24;color:var(--ink)}
  .note.right{text-align:right}
  .note b{font-weight:700}
</style>
</head>
<body>
<main class="poster">
  <svg class="header-shapes" width="1096" height="160" viewBox="0 0 1096 160">
    <path d="M0 0 H470 L410 78 C300 86 170 110 0 150 Z" fill="var(--navy)"/>
    <path d="M470 0 H1096 V78 H410 Z" fill="var(--red)"/>
    <path d="M540 30 q12 14 32 12" stroke="#fff" stroke-width="3" fill="none" stroke-linecap="round"/>
    <path d="M740 44 q30 -6 62 -7" stroke="#fff" stroke-width="4" fill="none" stroke-linecap="round"/>
  </svg>
  <div class="brand">Pine Lark</div>
  <div class="headline-word">aina</div>
  <div class="headline-tag">That which feed us</div>

  <svg class="cycle" width="1096" height="772" viewBox="0 0 1096 772">
    <defs>
      <radialGradient id="treeTone" cx="50%" cy="45%" r="55%">
        <stop offset="0" stop-color="var(--tree-b)"/>
        <stop offset="1" stop-color="var(--tree-a)" stop-opacity=".35"/>
      </radialGradient>
      <marker id="arrow-red" viewBox="0 0 10 10" refX="5" refY="5" markerWidth="5" markerHeight="5" orient="auto"><path d="M0 0L10 5L0 10Z" fill="var(--red)"/></marker>
      <marker id="arrow-navy" viewBox="0 0 10 10" refX="5" refY="5" markerWidth="5" markerHeight="5" orient="auto"><path d="M0 0L10 5L0 10Z" fill="var(--navy)"/></marker>
      <marker id="arrow-teal" viewBox="0 0 10 10" refX="5" refY="5" markerWidth="5" markerHeight="5" orient="auto"><path d="M0 0L10 5L0 10Z" fill="var(--teal)"/></marker>
    </defs>
    <g transform="translate(-52 -198)">
      <circle cx="600" cy="600" r="218" fill="var(--sky)"/>
      <ellipse cx="600" cy="590" rx="100" ry="130" fill="url(#treeTone)" role="img" aria-label="Hand-drawn breadfruit tree with fruit, leaves and spreading roots"/>

      <g fill="none" stroke-width="4" stroke-linecap="round">
        <path d="M676 416 L700 428" stroke="var(--red)" marker-end="url(#arrow-red)"/>
        <path d="M812 578 L814 594" stroke="var(--teal)" marker-end="url(#arrow-teal)"/>
        <path d="M780 768 L770 780" stroke="var(--red)" marker-end="url(#arrow-red)"/>
        <path d="M630 846 L606 846" stroke="var(--navy)" marker-end="url(#arrow-navy)"/>
        <path d="M448 780 L440 770" stroke="var(--red)" marker-end="url(#arrow-red)"/>
        <path d="M414 616 L418 598" stroke="var(--teal)" marker-end="url(#arrow-teal)"/>
        <path d="M500 430 L516 420" stroke="var(--navy)" marker-end="url(#arrow-navy)"/>
      </g>

      <g stroke-width="10" fill="#fff">
        <circle cx="600" cy="402" r="72" stroke="var(--red)"/>
        <circle cx="786" cy="498" r="72" stroke="var(--teal)"/>
        <circle cx="812" cy="696" r="72" stroke="var(--red)"/>
        <circle cx="710" cy="846" r="72" stroke="var(--navy)"/>
        <circle cx="516" cy="846" r="72" stroke="var(--red)"/>
        <circle cx="408" cy="696" r="72" stroke="var(--teal)"/>
        <circle cx="432" cy="498" r="72" stroke="var(--navy)"/>
      </g>

      <rect x="568" y="352" width="64" height="50" rx="10" fill="#e9b98f" role="img" aria-label="Two guests enjoying plant-based food"/>
      <g fill="#1b1b1b">
        <rect x="768" y="456" width="36" height="6" rx="2"/>
        <rect x="780" y="450" width="12" height="5" rx="2"/>
        <path d="M770 466 H802 L798 508 H774 Z"/>
        <rect x="778" y="472" width="3" height="30" fill="#fff"/>
        <rect x="785" y="472" width="3" height="30" fill="#fff"/>
        <rect x="792" y="472" width="3" height="30" fill="#fff"/>
      </g>
      <circle cx="812" cy="672" r="26" fill="#6cb33f" role="img" aria-label="Green recycling arrows"/>
      <rect x="684" y="796" width="54" height="48" rx="6" fill="#8c6a45" role="img" aria-label="Person turning a wooden compost bin"/>
      <rect x="494" y="796" width="46" height="48" rx="8" fill="#e8a531" role="img" aria-label="Sack of rich soil with trowel"/>
      <ellipse cx="408" cy="670" rx="32" ry="26" fill="#9ec94a" role="img" aria-label="Sliced breadfruit and green leaves"/>
      <ellipse cx="432" cy="474" rx="28" ry="22" fill="#e1b24c" role="img" aria-label="Mixing bowl with whisk"/>
    </g>
  </svg>

  <div class="step-label" style="left:483px;top:212px">Foodie<br>Experience</div>
  <div class="step-label" style="left:669px;top:316px">Zero<br>Waste</div>
  <div class="step-label" style="left:695px;top:520px">We Recycle</div>
  <div class="step-label" style="left:593px;top:674px">Compost</div>
  <div class="step-label" style="left:399px;top:654px">Healthy<br>Soil</div>
  <div class="step-label" style="left:291px;top:520px">Canoe Plants</div>
  <div class="step-label" style="left:315px;top:316px">Food<br>Preparation</div>

  <p class="note" style="left:648px;top:154px;width:310px">Make memories of snorkeling in beautiful Kealakekua and enjoy an exclusive foodie experience of <b>healthful, plant-based cuisine</b> as you've never experienced before.</p>
  <p class="note" style="left:826px;top:286px;width:232px">Pine Lark snorkel tours are <b>zero-waste</b> and do not produce trash for the landfill.</p>
  <p class="note" style="left:852px;top:446px;width:210px">We <b>recycle</b> all cardboard, cans, and bottles. Any leftover or waste products from our kitchen and meals are collected for composting on our farm.</p>
  <p class="note" style="left:746px;top:624px;width:300px">The organic materials we collect break down over time into nutrient-rich <b>compost</b> which we use on our farm to grow produce served on our tours.</p>
  <p class="note right" style="left:14px;top:624px;width:364px"><b>Healthy soil</b>, rich in nutrients and organic matter, starts with how we treat our ʻaina. Our family farm follows organic, bio-dynamic, and Korean Natural Farming practices, preparing the soil for planting.</p>
  <p class="note right" style="left:10px;top:430px;width:258px">The organic produce we serve is nutrient-dense and flavorful and features some <b>traditional Hawaiian "canoe plants"</b> - plants the first Hawaiians brought to Hawaiʻi from Polynesia for food - like ʻulu (breadfruit), ʻuala (purple sweet potato) &amp; maiʻa (banana).</p>
  <p class="note right" style="left:20px;top:266px;width:268px">All food is prepared daily from scratch in our <b>100% plant-based kitchen</b> with taste and nutritional content in mind, as well as being cruelty-free towards animals and the environment.</p>

  <div class="bottom-rule"></div>
</main>
</body>
</html>
```